Patient Engagement Solution

We need an attractive and easy-to-use GUI for patients and clinicians, which includes screens and icons. The application has been named Quorvix. I have our corporate logo attached as well.
I have attached the screens that the developer has used to create the solution, but we all know they miss the target when it comes to the creative stuff.
If it helps, I can supply some competitor's screens as a guide - please let me know.

Target Market(s)

Patients and Clinicians

Industry/Entity Type

Healthcare/Hospitals

Font styles to use
Other font styles liked:
• Easy to Read

Requirements
Must have
• Attractive, easy to use graphical user interface. Screen size is usually 22" 16:9
Nice to have
• Inviting and interesting look
Should not have
• Complicated hard to navigate screens

```html
<!DOCTYPE html>
<html lang="en">
<head>
<meta charset="utf-8">
<title>Quorvix – Entertainment</title>
<link href="https://fonts.googleapis.com/css2?family=Inter:wght@500;600&display=swap" rel="stylesheet">
<style>
  :root {
    --tile: #ff7852;
    --tile-glow: #ffb39c;
    --tile-icon: #ff7852;
    --icon-bg: #ffffff;
    --ink: #0d0d0d;
    --brand: #1596cf;
    --back-bg: #ece9cf;
    --back-ink: #1d2330;
  }
  * { margin: 0; padding: 0; box-sizing: border-box; }
  html, body { width: 1200px; height: 675px; overflow: hidden; }
  body {
    font-family: "Inter", sans-serif;
    position: relative;
    background:
      radial-gradient(ellipse 300px 260px at 120px 200px, rgba(150,248,255,0.95), rgba(150,248,255,0) 70%),
      radial-gradient(ellipse 330px 220px at 980px 110px, rgba(178,200,255,0.95), rgba(178,200,255,0) 72%),
      radial-gradient(ellipse 220px 180px at 1120px 600px, rgba(176,214,255,0.9), rgba(176,214,255,0) 70%),
      radial-gradient(ellipse 360px 170px at 330px 640px, rgba(255,255,190,0.95), rgba(255,255,190,0) 72%),
      radial-gradient(ellipse 200px 160px at 80px 600px, rgba(170,236,215,0.9), rgba(170,236,215,0) 70%),
      radial-gradient(ellipse 260px 200px at 1000px 300px, rgba(245,235,255,0.8), rgba(245,235,255,0) 70%),
      #f4feff;
  }
  .brand {
    position: absolute; top: 17px; left: 0; width: 1200px;
    text-align: center; font-size: 27px; font-weight: 600;
    color: var(--brand); letter-spacing: 0.5px;
  }
  .page-title {
    position: absolute; top: 168px; left: 0; width: 1200px;
    text-align: center; font-size: 45px; font-weight: 600; color: var(--ink);
  }
  .tile {
    position: absolute; top: 280px; width: 131px; height: 115px;
    border-radius: 15px;
    background:
      radial-gradient(circle 40px at 18px 14px, var(--tile-glow), rgba(255,179,156,0) 100%),
      var(--tile);
    color: #fff;
  }
  .tile .icon {
    position: absolute; left: 50%; top: 20px; transform: translateX(-50%);
    width: 43px; height: 43px; border-radius: 10px; background: var(--icon-bg);
    display: flex; align-items: center; justify-content: center;
  }
  .tile .icon svg { width: 22px; height: 22px; stroke: var(--tile-icon); fill: none; stroke-width: 1.8; stroke-linecap: round; stroke-linejoin: round; }
  .tile .label {
    position: absolute; left: 0; width: 100%; top: 74px;
    text-align: center; font-size: 16px; font-weight: 500;
  }
  .tile--focused {
    top: 268px; width: 158px; height: 139px; border-radius: 18px;
    box-shadow: 0 14px 14px -8px rgba(220,90,60,0.45);
  }
  .tile--focused .icon { top: 24px; width: 52px; height: 52px; border-radius: 12px; }
  .tile--focused .icon svg { width: 26px; height: 26px; }
  .tile--focused .label { top: 90px; font-size: 18px; }
  .back {
    position: absolute; left: 537px; top: 597px; width: 124px; height: 41px;
    border-radius: 12px; background: var(--back-bg); color: var(--back-ink);
    display: flex; align-items: center; justify-content: center; gap: 12px;
    font-size: 15px; font-weight: 500;
  }
  .back svg { width: 16px; height: 16px; stroke: var(--back-ink); fill: none; stroke-width: 1.8; stroke-linecap: round; stroke-linejoin: round; }
</style>
</head>
<body>
  <div class="brand">Quorvix</div>
  <h1 class="page-title">Entertainment</h1>

  <div class="tile" style="left:159px">
    <div class="icon"><svg viewBox="0 0 24 24"><rect x="3" y="7" width="18" height="13" rx="2.5"/><path d="M8 3l4 4 4-4"/><path d="M10.5 11v5l4-2.5z"/></svg></div>
    <div class="label">Watch TV</div>
  </div>
  <div class="tile tile--focused" style="left:333px">
    <div class="icon"><svg viewBox="0 0 24 24"><path d="M7 4.5v15l12-7.5z"/></svg></div>
    <div class="label">Movies</div>
  </div>
  <div class="tile" style="left:534px">
    <div class="icon"><svg viewBox="0 0 24 24"><circle cx="7" cy="18" r="2.2"/><circle cx="17" cy="16" r="2.2"/><path d="M9.2 18V6l10-2v12"/></svg></div>
    <div class="label">Music</div>
  </div>
  <div class="tile" style="left:721px">
    <div class="icon"><svg viewBox="0 0 24 24"><rect x="3" y="8" width="18" height="12" rx="2"/><path d="M6 8l11-4"/><path d="M3 12h18"/><path d="M14 16h.01M17 16h.01"/></svg></div>
    <div class="label">Radio</div>
  </div>
  <div class="tile" style="left:908px">
    <div class="icon"><svg viewBox="0 0 24 24"><path d="M7 6h10a4 4 0 014 4l1 7a2.5 2.5 0 01-4.5 1.5L15 16H9l-2.5 2.5A2.5 2.5 0 012 17l1-7a4 4 0 014-4z"/><path d="M7 10v3M5.5 11.5h3"/><path d="M15 11h.01M17 13h.01"/></svg></div>
    <div class="label">Games</div>
  </div>

  <div class="back">
    <svg viewBox="0 0 24 24"><path d="M20 12H4M10 6l-6 6 6 6"/></svg>
    <span>Back</span>
  </div>
</body>
</html>
```